Brondale custom business card design

After a business card incorporating the attached logo, I want the following

Brondale
-Aluminium Windows & doors
-cladding
-roof access systems
-labour hire
-disabled access audits and alterations
-general carpentry

F 7, 21 marlow creek road, Tarrowby 3912
Ph: 5837 2194
Fax: 5837 2158
Mob: 0400 731 592
Mitchell@brondaletrade.example

Target Market(s)

Construction industry

Industry/Entity Type

Business

Contact Information for Business Card

As per brief

Font styles to use
Serif
Script

```html
<!DOCTYPE html>
<html lang="en">
<head>
<meta charset="utf-8">
<title>Brondale – Business Card</title>
<link rel="stylesheet" href="https://fonts.googleapis.com/css2?family=Open+Sans:wght@400;600;700&display=swap">
<style>
  :root {
    --page-bg: #e9e7e3;
    --card-white: #ffffff;
    --band-grey: #f1f1f1;
    --ink: #1c1c1c;
    --ink-soft: #4a4a4a;
    --rule: #2a2a2a;
    --watermark: #ececec;
    --back-dark: #2a2a2a;
    --back-light: #4a4a4a;
    --back-text: #ffffff;
  }
  * { box-sizing: border-box; margin: 0; padding: 0; }
  html, body {
    width: 1200px; height: 913px; overflow: hidden;
    background: var(--page-bg);
    font-family: "Open Sans", Arial, sans-serif;
    color: var(--ink);
  }
  .stage {
    position: relative; width: 1200px; height: 913px;
    display: flex; align-items: center; justify-content: center; gap: 60px;
  }
  .card {
    position: relative; width: 520px; height: 316px;
    border-radius: 18px; overflow: hidden;
    box-shadow: 0 6px 18px rgba(0,0,0,.18);
  }
  /* Front */
  .card-front { background: var(--card-white); }
  .services-band {
    position: absolute; left: 0; top: 0; width: 100%; height: 108px;
    background: var(--band-grey);
  }
  .services-list {
    position: absolute; left: 300px; top: 16px;
    list-style: disc; padding-left: 14px;
    font-size: 10.5px; line-height: 14px; color: var(--ink-soft);
  }
  .watermark-name {
    position: absolute; right: 26px; top: 120px;
    font-size: 50px; font-weight: 700; color: var(--watermark);
    letter-spacing: 1px; line-height: 1;
  }
  .front-name {
    position: absolute; left: 34px; top: 124px;
    font-size: 36px; font-weight: 700; color: var(--ink); line-height: 1;
  }
  .contact {
    position: absolute; left: 34px; top: 184px; width: 460px;
    font-size: 11.5px; color: var(--ink-soft);
  }
  .contact-row { display: flex; align-items: center; gap: 8px; height: 18px; white-space: nowrap; }
  .contact-row svg { width: 11px; height: 11px; flex: none; }
  .contact-rule { border-top: 1.5px solid var(--rule); width: 170px; margin: 8px 0 6px; }
  .phone-row { font-size: 14px; font-weight: 700; color: var(--ink); height: 19px; }
  /* Back */
  .card-back {
    background: radial-gradient(ellipse at 50% 45%, var(--back-light) 0%, var(--back-dark) 70%);
    display: flex; align-items: center; justify-content: center;
  }
  .back-name {
    font-size: 56px; font-weight: 700; color: var(--back-text);
  }
</style>
</head>
<body>
<main class="stage">
  <section class="card card-front" aria-label="Business card front">
    <div class="services-band"></div>
    <ul class="services-list">
      <li>Aluminium Windows &amp; doors</li>
      <li>Cladding</li>
      <li>Roof access systems</li>
      <li>Labour hire</li>
      <li>Disabled access audits and alterations</li>
      <li>General carpentry</li>
    </ul>
    <div class="watermark-name" aria-hidden="true">Brondale</div>
    <h1 class="front-name">Brondale</h1>
    <div class="contact">
      <div class="contact-row">
        <svg viewBox="0 0 12 12"><circle cx="6" cy="6" r="5.5" fill="none" stroke="currentColor"/><path d="M6 2.5a2 2 0 0 0-2 2c0 1.6 2 4 2 4s2-2.4 2-4a2 2 0 0 0-2-2z" fill="currentColor"/></svg>
        <span>F 7, 21 marlow creek road, Tarrowby 3912</span>
      </div>
      <div class="contact-row">
        <svg viewBox="0 0 12 12"><circle cx="6" cy="6" r="5.5" fill="none" stroke="currentColor"/><rect x="3" y="4" width="6" height="4" fill="none" stroke="currentColor" stroke-width=".9"/><path d="M3 4l3 2.2L9 4" fill="none" stroke="currentColor" stroke-width=".9"/></svg>
        <span>Mitchell@brondaletrade.example</span>
      </div>
      <div class="contact-rule"></div>
      <div class="contact-row phone-row">
        <svg viewBox="0 0 12 12"><circle cx="6" cy="6" r="5.5" fill="none" stroke="currentColor"/><path d="M4 3.2l1 1.3-.6.7c.4.9 1 1.5 1.9 1.9l.7-.6 1.3 1-.6 1.1C5.5 8.4 3.6 6.5 3 4z" fill="currentColor"/></svg>
        <span>5837 2194</span>
      </div>
      <div class="contact-row phone-row">
        <svg viewBox="0 0 12 12"><circle cx="6" cy="6" r="5.5" fill="none" stroke="currentColor"/><rect x="4.4" y="2.8" width="3.2" height="6.4" rx=".6" fill="none" stroke="currentColor" stroke-width=".9"/></svg>
        <span>0400 731 592</span>
      </div>
      <div class="contact-row phone-row">
        <svg viewBox="0 0 12 12"><circle cx="6" cy="6" r="5.5" fill="none" stroke="currentColor"/><rect x="3" y="5" width="6" height="3.5" fill="none" stroke="currentColor" stroke-width=".9"/><rect x="4" y="3" width="4" height="2" fill="none" stroke="currentColor" stroke-width=".9"/></svg>
        <span>5837 2158</span>
      </div>
    </div>
  </section>
  <section class="card card-back" aria-label="Business card back">
    <div class="back-name">Brondale</div>
  </section>
</main>
</body>
</html>
```